Process infographic

Introducing Tessa – the virtual restaurant experience at home

Missing going out on dining at your favourite restaurant with your friends, then Tessa Dining is the answer.

While it may not be possible during the COVID-19 pandemic, or when restaurants return as booking opportunities will be hard to get, an innovative new concept gives people the chance to enjoy a virtual restaurant experience at home.

TESSA offers diners the ability to get the restaurant experience at home and restaurants to expand their dining rooms beyond the confines of social distancing

Tessa Dining is an app where you can book your favourite restaurant table, invite your friends and choose your menu and beverages. On the day the restaurant will come to your house, set your table, cook and serve you the menu you have chosen, serve you drinks and clean up, just like you where at the restaurant.

We are looking for 2 similar infographics to explain a process from 2 different perspective

The design needs to be simple, contemporary, imaginative and modern for this concept, it needs to be sophisticated, something that would represent an up-market to fine dining style of restaurant. The designs need to be easily understood using white space to separate the elements

Our preferred colour is attached along with our logos

Infographic 1 - Host Process
1. Host makes reservation at favourite restaurant at home on the Tessa Dining App
2. Select menus and invite guests
3. Confirm either single or shared payment options
4. Booking confirmed with restaurant
5. Host confirms on the App they the required equipment
6. Cook/server arrive 1 hour prior to guests, prepares and sets table
7. Guests arrive and cook/server offer dinks and serves meal
8. Cook/Server cleans up and finalises check with host

Infographic 2 - Restaurant Process
1. Host makes reservation and orders meal
2. Restaurant confirm reservation details
3. Restaurant prepares cuisine and arranges cook/serve waiter
4. Cook/server arrive 1 hour before guests, prepares and sets table
5. Cook/server cooks and serves meals and wine
6. Cook/Server cleans up and finalises check with host

Good Luck

```html
<!DOCTYPE html>
<html lang="en">
<head>
<meta charset="utf-8">
<title>Host Process – Tessa Dining</title>
<link rel="stylesheet" href="https://fonts.googleapis.com/css2?family=Lato:wght@400;900&family=Arimo:wght@700&display=swap">
<style>
  :root {
    --bg-top: #513449;
    --bg-bottom: #2d1929;
    --band: #4f3249;
    --pattern-top: #4a2e43;
    --pattern-bottom: #2b1727;
    --gold: #b08a55;
    --line: #ffffff;
    --text: #ffffff;
  }
  * { margin: 0; padding: 0; box-sizing: border-box; }
  html, body { width: 1200px; height: 1158px; overflow: hidden; }
  body {
    position: relative;
    background: linear-gradient(to bottom, var(--bg-top) 0%, var(--bg-top) 55%, var(--bg-bottom) 100%);
    font-family: "Lato", sans-serif;
    color: var(--text);
  }
  .pattern-column {
    position: absolute;
    left: 280px; top: 0;
    width: 640px; height: 1158px;
    background:
      linear-gradient(to bottom, rgba(176,138,85,0.12), rgba(176,138,85,0.08)),
      linear-gradient(to bottom, var(--pattern-top), var(--pattern-bottom));
  }
  .title-plate {
    position: absolute;
    left: 428px; top: 55px;
    width: 340px; height: 44px;
    background: var(--bg-top);
    display: flex; align-items: center; justify-content: center;
  }
  .title {
    font-family: "Lato", sans-serif;
    font-weight: 900;
    font-size: 28px;
    letter-spacing: 0.32em;
    padding-left: 0.32em;
    color: var(--text);
  }
  .ribbons { position: absolute; left: 0; top: 0; }
  .step {
    position: absolute;
    left: 258px;
    width: 684px;
    height: 80px;
    display: flex;
    align-items: center;
  }
  .step-number {
    width: 156px;
    padding-left: 96px;
    font-family: "Arimo", sans-serif;
    font-weight: 700;
    font-size: 44px;
    line-height: 1;
    text-align: center;
  }
  .step-text {
    font-size: 19.5px;
    line-height: 24px;
    font-weight: 400;
    letter-spacing: 0.01em;
  }
</style>
</head>
<body>
  <div class="pattern-column" role="img" aria-label="Gold geometric lattice pattern running down the centre column"></div>

  <div class="title-plate"><h1 class="title">HOST PROCESS</h1></div>

  <svg class="ribbons" width="1200" height="1158" viewBox="0 0 1200 1158" aria-hidden="true">
    <defs>
      <g id="ribbon">
        <rect x="258" y="0" width="684" height="79" fill="var(--band)"/>
        <path d="M280,-22 Q258,-22 258,-11 Q258,0 280,0 L920,0 Q942,0 942,11 L942,90 Q942,101 920,101"
              fill="none" stroke="var(--line)" stroke-width="1.2"/>
        <path d="M258,-11 L258,71 Q258,79 272,79 L920,79 Q942,79 942,90"
              fill="none" stroke="var(--line)" stroke-width="1.2"/>
      </g>
    </defs>
    <use href="#ribbon" y="160"/>
    <use href="#ribbon" y="279"/>
    <use href="#ribbon" y="398"/>
    <use href="#ribbon" y="517"/>
    <use href="#ribbon" y="636"/>
    <use href="#ribbon" y="755"/>
    <use href="#ribbon" y="874"/>
    <use href="#ribbon" y="993"/>
  </svg>

  <ol class="steps">
    <li class="step" style="top:160px"><span class="step-number">1</span><span class="step-text">Host makes reservation at favourite restaurant<br>at home on the Tessa Dining App</span></li>
    <li class="step" style="top:279px"><span class="step-number">2</span><span class="step-text">Select menus and invite guests</span></li>
    <li class="step" style="top:398px"><span class="step-number">3</span><span class="step-text">Confirm either single or shared payment options</span></li>
    <li class="step" style="top:517px"><span class="step-number">4</span><span class="step-text">Booking confirmed with restaurant</span></li>
    <li class="step" style="top:636px"><span class="step-number">5</span><span class="step-text">Host confirms on the App the required equipment</span></li>
    <li class="step" style="top:755px"><span class="step-number">6</span><span class="step-text">Cook/server arrive 1 hour prior to guests,<br>prepares and sets table</span></li>
    <li class="step" style="top:874px"><span class="step-number">7</span><span class="step-text">Guests arrive and cook/server offer drinks<br>and serves meal</span></li>
    <li class="step" style="top:993px"><span class="step-number">8</span><span class="step-text">Cook/Server cleans up and finalises check with host</span></li>
  </ol>
</body>
</html>
```